Medical Internet Marketing Company Needs a Site!

We need a new, fresh website for our search engine optimization and social media marketing company. We specialize in helping medical practices, doctors, physicians, and hospitals with their online presence and web ranking. The site should lean towards being suited for these audiences.

We have several examples of website that we like as well as things that we like about them.

Here are sites that we enjoy.

www.brightwavelab.com

It's a good design for the site all around. The videos, buttons, and images are all excellent. They did a fine job.

- We really like their "contact us" side bar and want to include one like it on the secondary pages.

www.corvantis.net

- We don't like the "thickness" of the top navigation bar.
- We like the page colors, easy navigation, and big call to action phone number in the top right corner.

http://www.teluvo.com/

Out of all the examples provided, Teluvo is our favorite and closest look and style to what we are looking for.

- We really like the openness of the design, such as space between the text and background.

- We want a price page in a style very similar to their pricing page with the services listed and check-marks, etc. although we intend to have multiple service package columns much like Corvantis's SEO pricing page.

- The way the video fits into the home page header is very organized, simple, and attention grabbing. We intend to place a slider with videos here.

- We need a page design that will allow for an image slider like Teluvo's Features page.

Here's a great example of a medical internet marketing website: http://www.dermaplex.com/

Target Market(s)

Our target market is doctors, typically male and typically 40-45 years old. I

Industry/Entity Type

Marketing

Requirements
Must have
• The homepage should have a slider in the video. Interior pages should have a video in the very top similar to how they do it on www.brightwavelab.com

The top navigation tabs needed are:
- Home
- Solutions
- Resources
- About
- Why Quelvo
- Contact

The sidebar should have a GREAT call to action in it on interior pages.

There should be one interior page that is similar to this - http://www.teluvo.com/pricing/

There needs to be a page with multiple boxes that take up a row of the web page's body. This page will house all the case studies similar to brightwave lab's: http://www.brightwavelab.com/success-stories/case-studies/ The one exception is we want the case studies to be inside of "boxes" instead of between horizontal lines like brightwave lab's.
Nice to have
• Color, professional, and clean. GREAT use of calls to actions.

```html
<!DOCTYPE html>
<html lang="en">
<head>
<meta charset="utf-8">
<title>Quelvo — Medical Internet Marketing</title>
<link rel="stylesheet" href="https://fonts.googleapis.com/css2?family=Arimo:ital,wght@0,400;0,700;1,400&family=Gelasio:ital@1&display=swap">
<style>
:root{
  --canvas:#2e2e2e;
  --page:#f6f6f6;
  --white:#ffffff;
  --band:#e9e9e9;
  --ink:#222222;
  --grey:#8f8f8f;
  --logo-grey:#9d9d9d;
  --green:#8dc63f;
  --news-green:#7ab317;
  --body-text:#a8602c;
  --intro-text:#10245a;
  --footer:#222324;
  --footer-head:#d2d2d2;
  --footer-text:#7c7c7c;
  --footer-link:#8d8d8d;
  --footer-rule:#2e2f30;
  --teal-text:#4f8c9a;
  --player:#2f3a1e;
  --player-bar:#4bb8c4;
}
*{box-sizing:border-box;margin:0;padding:0}
html,body{width:1172px;height:1200px;overflow:hidden}
body{background:var(--canvas);font-family:"Arimo",Arial,sans-serif;color:var(--ink);position:relative}
.page{position:absolute;left:89px;top:16px;width:1022px;height:900px;background:var(--page);border-radius:4px 4px 0 0}
.abs{position:absolute}

.main-nav{left:231px;top:-5px;width:763px;height:48px;background:linear-gradient(#f2f2f2,#d9d9d9);border:1px solid #c4c4c4;border-top:none;border-radius:0 0 10px 10px;display:flex;align-items:center;padding-left:13px}
.main-nav a{font-size:15px;color:#3a3a3a;text-decoration:none;padding:8px 19px;line-height:18px}
.main-nav a.is-active{background:linear-gradient(#e2e2e2,#cfcfcf);border:1px solid #b8b8b8;border-radius:2px;padding:7px 20px}

.brand{left:33px;top:64px;display:flex;align-items:center;gap:14px}
.brand-mark{width:44px;height:44px;background:var(--green)}
.brand-name{font-size:58px;letter-spacing:4px;color:var(--logo-grey);font-weight:400;line-height:1}

.call-line{right:34px;top:66px;display:flex;align-items:center;gap:10px}
.call-line .label{font-size:15px;color:var(--grey)}
.call-line .number{font-size:21px;color:var(--ink)}

.hero{left:0;top:151px;width:1022px;height:281px;background:var(--white)}
.hero h1{position:absolute;left:17px;top:45px;font-size:28px;font-weight:400;color:var(--green)}
.hero p{position:absolute;left:17px;top:96px;width:460px;font-size:11px;line-height:18.5px;font-weight:700;color:var(--intro-text)}
.hero-video{position:absolute;left:536px;top:8px;width:453px;height:261px;background:radial-gradient(circle at 50% 35%,#d6ef6a,#a9d42c 70%)}
.player-play{position:absolute;left:16px;top:183px;width:101px;height:61px;background:var(--player);border-radius:4px;display:flex;align-items:center;justify-content:center}
.player-bar{position:absolute;left:130px;top:196px;width:317px;height:48px;background:var(--player);border-radius:4px}
.player-bar .progress{position:absolute;left:48px;top:17px;width:54px;height:14px;background:repeating-linear-gradient(90deg,var(--player-bar) 0 3px,transparent 3px 5px)}
.player-time{position:absolute;left:115px;top:181px;width:60px;height:22px;background:#fff;border-radius:2px;font-size:14px;letter-spacing:1px;display:flex;align-items:center;justify-content:center;color:#222}
.slider-dots{left:483px;top:443px;display:flex;gap:8px}
.slider-dots span{width:9px;height:9px;background:#f6b98a}
.slider-dots span:first-child{background:var(--green)}

.cta-band{left:0;top:453px;width:1022px;height:92px;background:var(--band);border-top:1px solid #d6d6d6;border-bottom:1px solid #d6d6d6}
.cta-band p{position:absolute;left:33px;top:29px;font-family:"Gelasio",Georgia,serif;font-style:italic;font-size:22px;color:#7a7a7a}
.btn-signup{position:absolute;left:873px;top:28px;width:116px;height:40px;background:linear-gradient(#444,#1e1e1e);border-radius:5px;color:#fff;font-size:15px;display:flex;align-items:center;justify-content:center}

.content{left:0;top:546px;width:1022px;height:354px}
.content-main{position:absolute;left:0;top:0;width:709px;height:354px;border-right:4px solid #e4e4e4}
.content-main h2{position:absolute;left:33px;top:32px;font-size:26px;font-weight:400;color:var(--ink)}
.why-text{position:absolute;left:33px;top:82px;width:642px;font-size:11.5px;line-height:18.5px;color:var(--body-text);text-align:justify}
.why-text p+p{margin-top:18px}
.why-photo{float:right;margin:0 0 8px 22px;width:225px;height:120px;border:1px solid #cfcfcf;background:linear-gradient(#7fb6df 0%,#a9cde6 30%,#4e7a3a 55%,#8a7a55 80%,#3f6a2e 100%)}
.soft-rule{position:absolute;left:70px;top:298px;width:500px;height:1px;background:linear-gradient(90deg,transparent,#d3d3d3,transparent)}

.news{position:absolute;left:744px;top:0;width:247px}
.news h3{margin-top:30px;font-size:21px;font-weight:400;color:var(--ink)}
.news ul{list-style:none;margin-top:12px}
.news li{font-size:11.5px;line-height:18px;color:var(--news-green);padding:5px 0 10px;border-bottom:1px dotted #bdbdbd}
.news li+li{padding-top:12px}
.btn-all{display:inline-flex;margin-top:18px;width:87px;height:30px;align-items:center;justify-content:center;border:1px solid #cacaca;border-radius:3px;background:linear-gradient(#fafafa,#e6e6e6);font-size:12px;color:#777}

.footer{position:absolute;left:89px;top:916px;width:1022px;height:237px;background:var(--footer);border-radius:0 0 3px 3px}
.footer-col{position:absolute;top:38px}
.footer-col h4{font-size:16px;font-weight:400;color:var(--footer-head);margin-bottom:14px}
.footer-col p,.footer-col li{font-size:11.5px;line-height:20px;color:var(--footer-text);list-style:none}
.footer-col .gap{margin-top:16px;line-height:17px;font-size:11px}
.footer-col .accent{color:var(--news-green)}
.footer-col .links li{color:var(--footer-link);line-height:21px}
.footer-divider{position:absolute;top:30px;width:1px;height:170px;background:var(--footer-rule)}
.social{display:flex;gap:9px;margin-top:-2px}
.social span{width:31px;height:31px;border-radius:50%;background:#f1f1f1;border:2px solid #cfcfcf}
.updates p{color:var(--teal-text);width:240px;line-height:19px}
.signup-form{display:flex;gap:4px;margin-top:18px}
.signup-form .field{width:145px;height:33px;border:1px solid #3c3c3c;background:#1b1b1c;color:#6d6d6d;font-size:11px;padding:10px 8px;border-radius:2px}
.signup-form .submit{width:79px;height:33px;background:linear-gradient(#3a3b3c,#2a2b2c);border:1px solid #444;color:#c8c8c8;font-size:12px;display:flex;align-items:center;justify-content:center;border-radius:2px}
</style>
</head>
<body>
<div class="page">
  <nav class="main-nav abs">
    <a class="is-active">Home</a><a>Solutions</a><a>Resources</a><a>About</a><a>Why Quelvo</a><a>Blog</a><a>Contact</a>
  </nav>

  <div class="brand abs">
    <span class="brand-mark"></span>
    <span class="brand-name">QUELVO</span>
  </div>

  <div class="call-line abs">
    <span class="label">For additional information call:</span>
    <span class="number">+00 987654321</span>
    <svg width="26" height="22" viewBox="0 0 26 22" aria-hidden="true">
      <path d="M2 8 C2 2 24 2 24 8 L24 10 L18 10 L18 7 L8 7 L8 10 L2 10 Z" fill="#111"/>
      <path d="M7 10 L19 10 L23 20 L3 20 Z" fill="#111"/>
      <circle cx="13" cy="15" r="3" fill="#fff"/>
    </svg>
  </div>

  <section class="hero abs">
    <h1>Easily Embed Video!</h1>
    <p>Lorem Ipsum is simply dummy text of the printing and typesetting industry. Lorem Ipsum has been the industry's standard dummy text ever since the 1500s, when an unknown printer took a galley of type and scrambled it to make a type specimen book.</p>
    <div class="hero-video" role="img" aria-label="Embedded video still: a cheerful cartoon house on a bright green sunburst background">
      <div class="player-play">
        <svg width="22" height="24" viewBox="0 0 22 24" aria-hidden="true"><path d="M2 1 L21 12 L2 23 Z" fill="#fff"/></svg>
      </div>
      <div class="player-time">01:44</div>
      <div class="player-bar">
        <svg class="abs" style="left:12px;top:17px" width="14" height="14" viewBox="0 0 14 14" aria-hidden="true"><rect x="1" y="1" width="12" height="12" fill="none" stroke="#cfd6c4" stroke-width="2"/></svg>
        <div class="progress"></div>
      </div>
    </div>
  </section>

  <div class="slider-dots abs"><span></span><span></span><span></span></div>

  <section class="cta-band abs">
    <p>Lorem Ipsum is simply dummy text of the printing and typesetting industry.</p>
    <div class="btn-signup">SIGN UP</div>
  </section>

  <section class="content abs">
    <div class="content-main">
      <h2>Why Choose Us?</h2>
      <div class="why-text">
        <div class="why-photo" role="img" aria-label="Photograph of a winding river between forested hills under a blue sky"></div>
        <p>Lorem Ipsum is simply dummy text of the printing and typesetting industry. Lorem Ipsum has been the industry's standard dummy text ever since the 1500s, when an unknown printer took a galley of type and scrambled it to make a type specimen book.</p>
        <p>It has survived not only five centuries, but also the leap into electronic typesetting, remaining essentially unchanged. It was popularised in the 1960s with the release of transfer sheets containing Lorem Ipsum passages, and more recently with desktop publishing software including versions of Lorem Ipsum.</p>
      </div>
      <div class="soft-rule"></div>
    </div>

    <aside class="news">
      <h3>Latest News</h3>
      <ul>
        <li>Consectetur adipiscing elit. Donec nunc ipsum, lobortis non convallis.</li>
        <li>Curabitur odio suscipit condimentum porttitor ut, egestas.</li>
        <li>Donec augue ligula, laoreet ornare nec, molestie vitae bibendum.</li>
      </ul>
      <span class="btn-all">All News</span>
    </aside>
  </section>
</div>

<footer class="footer">
  <div class="footer-col" style="left:33px">
    <h4>Contact Info</h4>
    <p>Phone: +00 987654321</p>
    <p>E-mail: info@quelvo.com</p>
    <p class="gap">Copyright @ 2012 • <span class="accent">QUELVO</span><br>All rights reserved</p>
  </div>
  <div class="footer-divider" style="left:264px"></div>
  <div class="footer-col" style="left:294px">
    <h4>Quick Menu</h4>
    <ul class="links"><li>About Us</li><li>Solutions</li><li>Resources</li><li>Why Quelvo</li></ul>
  </div>
  <div class="footer-divider" style="left:424px"></div>
  <div class="footer-col" style="left:455px">
    <h4>Stay Connected</h4>
    <div class="social"><span></span><span></span><span></span><span></span><span></span></div>
  </div>
  <div class="footer-divider" style="left:681px"></div>
  <div class="footer-col updates" style="left:714px">
    <h4>Email Updates</h4>
    <p>Information about current events related to our company</p>
    <div class="signup-form"><span class="field">-enter your e-mail-</span><span class="submit">Submit</span></div>
  </div>
</footer>
</body>
</html>
```